Finance Product Agency Business Card Design

We're an agency that provides products (service contracts, gap insurance, tire and wheel, etc) and support to dealership finance departments. We specialize in training finance producers to maximize their potential and also keep them up to date on the ever changing compliance and legal landscape. I'll attach an image of our logo, excited to see what you all come up with. Would also be interested in discussing our new website design with the winner.

Target Market(s)

auto dealerships

Industry/Entity Type

Business

Contact Information for Business Card

Dale Hoskirk
Phone 517.364.2908
Fax 877.245.3196
email Dale.Hoskirk@brightlanecoverage.com

Requirements
Must have
• basic contact information
Nice to have
• looking for something professional but modern

```html
<!DOCTYPE html>
<html lang="en">
<head>
<meta charset="utf-8">
<title>Brightlane Coverage – Business Card</title>
<link rel="stylesheet" href="https://fonts.googleapis.com/css2?family=Montserrat:wght@400;600;800&display=swap">
<style>
  :root {
    --backdrop: #d9dcde;
    --teal-dark: #163a44;
    --teal: #1f4f5c;
    --teal-light: #2e6876;
    --silver-light: #f4f5f5;
    --silver: #d7dadb;
    --silver-dark: #b9bdbf;
    --rule: #e8eef0;
    --ink-light: #eef4f5;
    --mark: #23505c;
  }
  * { box-sizing: border-box; margin: 0; padding: 0; }
  html, body { width: 1200px; height: 750px; overflow: hidden; }
  body {
    background: var(--backdrop);
    font-family: "Montserrat", sans-serif;
    position: relative;
  }
  .card {
    position: absolute;
    width: 520px;
    height: 300px;
    border-radius: 22px;
    overflow: hidden;
    background: linear-gradient(180deg, var(--teal-light), var(--teal) 45%, var(--teal-dark));
    box-shadow: 0 10px 24px rgba(0,0,0,0.25);
  }
  .card--contact { left: 50px; top: 100px; }
  .card--brand { left: 630px; top: 350px; }

  .band {
    position: absolute;
    left: 0; right: 0;
    background: linear-gradient(180deg, var(--silver-light), var(--silver) 70%, var(--silver-dark));
    border-top: 3px solid var(--teal-dark);
    border-bottom: 3px solid var(--teal-dark);
    outline: 2px solid var(--rule);
    outline-offset: 3px;
    display: flex;
    align-items: center;
    justify-content: center;
  }
  .card--contact .band { top: 42px; height: 108px; }
  .card--brand .band { top: 66px; height: 168px; }

  .brand {
    display: flex;
    align-items: center;
    gap: 12px;
  }
  .brand__dot {
    width: 30px; height: 30px;
    border-radius: 50%;
    background: var(--mark);
  }
  .brand__name {
    font-weight: 800;
    color: var(--mark);
    text-transform: uppercase;
    letter-spacing: 0.5px;
    font-size: 24px;
  }
  .card--brand .brand__dot { width: 40px; height: 40px; }
  .card--brand .brand__name { font-size: 31px; }

  .wheel-mark {
    position: absolute;
    right: 24px; top: 150px;
    width: 120px; height: 120px;
    border-radius: 50%;
    background: radial-gradient(circle, rgba(255,255,255,0.06), rgba(255,255,255,0.12));
  }

  .contact {
    position: absolute;
    left: 40px; top: 168px;
    color: var(--ink-light);
  }
  .contact__name {
    font-weight: 600;
    font-size: 17px;
    letter-spacing: 1.5px;
    text-transform: uppercase;
    padding-bottom: 6px;
    border-bottom: 1px solid rgba(238,244,245,0.7);
    display: inline-block;
    padding-right: 40px;
  }
  .contact__lines {
    margin-top: 14px;
    font-size: 12.5px;
    letter-spacing: 1px;
    line-height: 1.9;
  }
  .contact__row { display: flex; gap: 26px; }
  .contact__item { display: inline-flex; align-items: center; gap: 7px; }
  .contact__item svg { width: 14px; height: 14px; fill: var(--ink-light); }
  .contact__email { font-variant: small-caps; font-size: 13px; }
</style>
</head>
<body>

  <section class="card card--contact">
    <div class="band">
      <div class="brand">
        <span class="brand__dot"></span>
        <span class="brand__name">Brightlane Coverage</span>
      </div>
    </div>
    <div class="wheel-mark" role="img" aria-label="Faint steering wheel decoration"></div>
    <div class="contact">
      <div class="contact__name">Dale Hoskirk</div>
      <div class="contact__lines">
        <div class="contact__row">
          <span class="contact__item">
            <svg viewBox="0 0 16 16" aria-hidden="true"><path d="M3.6 1.5l2.3 2.4-1.3 2a9 9 0 0 0 5.5 5.5l2-1.3 2.4 2.3-1.6 2.1C7.6 14.4 1.6 8.4 1.5 3.1z"/></svg>
            517.364.2908
          </span>
          <span class="contact__item">
            <svg viewBox="0 0 16 16" aria-hidden="true"><path d="M4 1h8v4H4zM2 6h12a1 1 0 0 1 1 1v5h-3v3H4v-3H1V7a1 1 0 0 1 1-1zm3 5v3h6v-3z"/></svg>
            877.245.3196
          </span>
        </div>
        <div class="contact__email">Dale.Hoskirk@brightlanecoverage.com</div>
      </div>
    </div>
  </section>

  <section class="card card--brand">
    <div class="band">
      <div class="brand">
        <span class="brand__dot"></span>
        <span class="brand__name">Brightlane Coverage</span>
      </div>
    </div>
  </section>

</body>
</html>
```